In Store POP Material Design

From: Derek Holm
Sent: Wednesday, October 10, 2012 7:35 AM
To: 'Neil Farrow'
Subject: Marketing Brief for S7 branding
We are looking to create a new look and feel for our Steadfast Coverage (s7) branded materials.
We sell extended service plans through retailers and manufacturers throughout North America.
The store sales personnel offer an extended warranty with the purchase of an Appliance, TV, computer, Camera etc.
We also want these materials to allow for us to include client logos so that we can leverage their brands to add value. I have included our old S7 brochure, a new concept for our Brevin store clients and another client named Oxley as reference
Our objective is to create in store tools (brochures, posters, stickers) etc to help the sales people close more sales. We are positioning our protection plans as part of a "total solution" sale. For example, if you buy a TV, you would also need to buy a mount, HDMI cable, screen cleaner etc. In our materials we want to illustrate this and help the sales person not only sell our warranty but the other accessories and services as well.
We also want to create a standard look and feel that is very info-graphic in nature. Heavy use of icons and a web 2.0 type of feel.
Have a look at some of these Infographics and you'll get an idea what I mean.
http://chartlumen.com/wp-content/uploads/2012/05/HDTV-Comparison-LCD-vs.-Plasma.jpg
http://plotquarry.com/wp-content/uploads/2011/04/Handset_Infographic_800px.jpg
My favorite sites are
http://www.glyphmeadow.info/
http://www.ribbonvane.com/
You can reference info on our programs through our corporate website:
http://www.thek9option.com/extended-warranty-solutions
Bottom line, we want to create a new look and feel for the S7 brand and then tie whatever we come up with into both online and in-store materials.
The winner of this design contest will have plenty of work through this project as well as our other companies which you will find at: www.theholmgroup.ca
Derek Holm
Holm Group of Companies | www.theholmgroup.ca
K9 Options | HGX Manufacturing | TalonGate Security
T: 1.604.555.0183 | M: 1.604.555.0147
E: derek.holm@theholmgroup.ca

```html
<!DOCTYPE html>
<html lang="en">
<head>
<meta charset="utf-8">
<title>S7 Steadfast Coverage Plan – In-Store Card</title>
<link rel="stylesheet" href="https://fonts.googleapis.com/css2?family=Arimo:wght@400;700&family=Barlow:wght@400;500&family=Open+Sans:wght@400&display=swap">
<style>
  :root{
    --navy:#1b4a63;
    --cyan:#00aeef;
    --feature-blue:#0d4f78;
    --heading-teal:#1d5c7c;
    --key-cyan:#1ea5dc;
    --body-grey:#555a5e;
    --rule-grey:#b9bcbf;
    --receipt-bg:#e6e7e8;
    --receipt-text:#9a9c9e;
    --seg-blue:#45a9d6;
    --seg-grey:#d8d9da;
  }
  *{margin:0;padding:0;box-sizing:border-box}
  html,body{width:1065px;height:1200px;overflow:hidden;background:#fff}
  body{font-family:"Arimo",Arial,sans-serif;color:var(--body-grey)}
  .card{position:relative;width:1065px;height:1200px;background:#fff}
  .edge-bar{position:absolute;width:15px}
  .edge-bar.navy{background:var(--navy)}
  .edge-bar.cyan{background:var(--cyan)}
  .left-panel{position:absolute;left:14px;top:285px;width:512px;height:915px;
    background:linear-gradient(#ffffff 0%,#f4f7f8 45%,#cfdbe0 100%)}
  .hero-photo{position:absolute;left:14px;top:0;width:512px;height:285px;
    background:linear-gradient(120deg,#e9eef0 0%,#cfdde3 35%,#f5f8f9 60%,#ffffff 100%)}
  .brand{position:absolute;left:122px;top:84px;display:flex;align-items:center;gap:28px;color:#1a1a1a;font-weight:700}
  .brand-mark{font-size:80px;line-height:1;letter-spacing:-3px}
  .brand-name{font-size:26px;line-height:25px;letter-spacing:-.6px}
  .tagline{position:absolute;left:60px;top:207px;width:390px;text-align:center;font-size:22px;line-height:26px;color:#222;letter-spacing:-.5px}
  .coverage-title{position:absolute;left:120px;top:307px;font-size:16px;color:#333}
  .coverage-title b{font-size:20px;margin-right:6px}
  .coverage-bar{position:absolute;left:78px;top:342px;display:flex;gap:2px}
  .coverage-bar span{height:21px;font-size:10px;font-weight:700;color:#fff;display:flex;align-items:center;justify-content:center}
  .coverage-bar .std{width:56px;background:linear-gradient(#fff,var(--seg-grey));color:#222;border-bottom:2px solid #888}
  .coverage-bar .ext{width:54px;background:var(--seg-blue)}
  .coverage-note{position:absolute;left:78px;top:373px;font-size:12px;line-height:16px;color:#333}
  .key-title{position:absolute;left:56px;top:432px;font-family:"Barlow",sans-serif;font-weight:400;font-size:34px;line-height:40px;color:var(--key-cyan)}
  .feature{position:absolute;left:48px;width:460px}
  .feature svg{position:absolute;left:0;top:2px}
  .feature h3{margin-left:41px;font-family:"Barlow",sans-serif;font-weight:400;font-size:24.5px;line-height:28px;color:var(--feature-blue)}
  .feature p{margin-left:41px;font-size:18.3px;line-height:22.4px;color:var(--body-grey)}
  .benefits{position:absolute;left:84px;top:948px;list-style:none}
  .benefits li{font-family:"Open Sans",sans-serif;font-size:19px;line-height:27.6px;color:#5a5e62;position:relative;padding-left:34px}
  .benefits li::before{content:"✓";position:absolute;left:0;color:var(--key-cyan);font-size:17px}
  .footnote{position:absolute;left:44px;top:1162px;font-size:11px;color:#555}
  .right-top{position:absolute;left:532px;top:0;width:518px;height:563px;background:linear-gradient(#dce4e8 0%,#ffffff 22%)}
  .steps-title{position:absolute;left:592px;top:96px;font-family:"Barlow",sans-serif;font-weight:400;font-size:42px;line-height:48px;color:var(--heading-teal)}
  .step-num{position:absolute;font-family:"Barlow",sans-serif;font-size:56px;color:#666;line-height:1}
  .step-text{position:absolute;left:645px;font-size:19.5px;line-height:24.4px;color:#555}
  .rule{position:absolute;height:1px;background:var(--rule-grey)}
  .receipt{position:absolute;left:532px;top:563px;width:518px;height:637px;background:var(--receipt-bg)}
  .receipt p{position:absolute;left:0;right:0;top:170px;text-align:center;font-family:"Open Sans",sans-serif;font-size:26px;letter-spacing:-.3px;color:var(--receipt-text)}
</style>
</head>
<body>
<div class="card">
  <div class="edge-bar navy" style="left:0;top:0;height:290px"></div>
  <div class="edge-bar cyan" style="left:0;top:302px;height:89px"></div>
  <div class="edge-bar navy" style="left:1050px;top:0;height:295px"></div>
  <div class="edge-bar cyan" style="left:1050px;top:302px;height:88px"></div>

  <div class="hero-photo" role="img" aria-label="Photo of a smiling couple in a bright home kitchen"></div>
  <div class="left-panel"></div>

  <div class="brand"><span class="brand-mark">S7</span><span class="brand-name">Steadfast<br>Coverage<br>Plan</span></div>
  <p class="tagline">Extends your appliance coverage<br>for up to 5 years from the<br>date of purchase.</p>

  <p class="coverage-title"><b>S7</b>Extended Coverage</p>
  <div class="coverage-bar">
    <span class="std">1 Year</span><span class="ext">2 Years</span><span class="ext">3 Years</span><span class="ext">4 Years</span><span class="ext">5 Years</span>
  </div>
  <p class="coverage-note">Standard<br>Manufacturer's<br>Warranty</p>

  <h2 class="key-title">Key Features</h2>

  <div class="feature" style="top:483px">
    <svg width="28" height="26" viewBox="0 0 28 26"><path d="M14 1 1 13h4v12h7v-8h4v8h7V13h4z" fill="#0d4f78"/></svg>
    <h3>In-Home Service</h3>
    <p>All repair service for major appliances<br>will be provided in your home by one<br>of our Authorized Service Technicians.</p>
  </div>
  <div class="feature" style="top:589px">
    <svg width="28" height="30" viewBox="0 0 28 30"><rect x="2" y="2" width="24" height="26" rx="2" fill="none" stroke="#0d4f78" stroke-width="2.5"/><line x1="2" y1="9" x2="26" y2="9" stroke="#0d4f78" stroke-width="2"/><rect x="6" y="13" width="16" height="11" fill="none" stroke="#0d4f78" stroke-width="2"/></svg>
    <h3>Major Component Coverage</h3>
    <p>Most manufacturers have reduced major<br>component coverage from 5 years<br>to just 1.&nbsp; With S7, you can cover these<br>components for up to 5 years.</p>
  </div>
  <div class="feature" style="top:720px">
    <svg width="28" height="30" viewBox="0 0 28 30"><rect x="4" y="3" width="20" height="3" fill="#0d4f78"/><rect x="11" y="0" width="6" height="3" fill="#0d4f78"/><path d="M6 8h16l-2 21H8z" fill="#0d4f78"/><g stroke="#fff" stroke-width="1.6"><line x1="11" y1="11" x2="11" y2="26"/><line x1="14" y1="11" x2="14" y2="26"/><line x1="17" y1="11" x2="17" y2="26"/></g></svg>
    <h3>Food Spoilage</h3>
    <p>S7 allows for $250 worth of frozen food<br>replacement during the term of the<br>extended coverage if food spoilage occurs<br>due to your freezer's mechanical failure.*</p>
  </div>
  <div class="feature" style="top:845px">
    <svg width="28" height="30" viewBox="0 0 28 30"><path d="M5 27C3 16 9 4 25 3c1 13-7 22-20 24z" fill="none" stroke="#0d4f78" stroke-width="2.5"/><path d="M6 26 20 9" stroke="#0d4f78" stroke-width="2"/></svg>
    <h3>Lemon Aid</h3>
    <p>Our customer service representatives will<br>arrange for the free replacement of the product<br>if the same component fails three times.</p>
  </div>

  <ul class="benefits">
    <li>Fully Insured for Your Protection</li>
    <li>Parts + Labour Coverage</li>
    <li>Toll-Free Support</li>
    <li>Fully Transferable</li>
    <li>Power Surge Protection</li>
    <li>No Deductible</li>
    <li>No Hidden Fees</li>
  </ul>
  <p class="footnote">*Refer to terms and conditions for further details</p>

  <div class="right-top"></div>
  <h1 class="steps-title">Service in 2 Easy Steps</h1>

  <span class="step-num" style="left:590px;top:212px">1</span>
  <p class="step-text" style="top:216px">Call us at 1 (866) 555-0199<br>to troubleshoot the problem.</p>
  <svg style="position:absolute;left:925px;top:210px" width="66" height="66" viewBox="0 0 66 66">
    <circle cx="33" cy="31" r="26" fill="none" stroke="#1ea5dc" stroke-width="5"/>
    <path d="M20 18c3-3 6-2 7 1l2 6c1 2 0 4-2 5 2 5 5 8 10 10 1-2 3-3 5-2l6 2c3 1 4 4 1 7-4 4-12 3-20-5S16 22 20 18z" fill="#1ea5dc"/>
    <ellipse cx="33" cy="62" rx="20" ry="3" fill="#d6eef8"/>
  </svg>

  <div class="rule" style="left:597px;top:297px;width:395px"></div>

  <span class="step-num" style="left:590px;top:327px">2</span>
  <p class="step-text" style="top:330px">If repair is required, we<br>will direct you to the nearest<br>authorized servicer or dispatch<br>a technician to your home.</p>
  <svg style="position:absolute;left:916px;top:330px" width="80" height="60" viewBox="0 0 80 60">
    <g stroke="#1ea5dc" stroke-width="3" stroke-linecap="round"><line x1="2" y1="14" x2="16" y2="14"/><line x1="6" y1="22" x2="16" y2="22"/><line x1="2" y1="30" x2="16" y2="30"/></g>
    <rect x="20" y="6" width="36" height="32" rx="2" fill="#1ea5dc"/>
    <path d="M58 16h12l8 12v10H58z" fill="#1ea5dc"/>
    <rect x="62" y="19" width="8" height="8" fill="#fff"/>
    <circle cx="32" cy="41" r="6" fill="#1ea5dc" stroke="#fff" stroke-width="2"/>
    <circle cx="68" cy="41" r="6" fill="#1ea5dc" stroke="#fff" stroke-width="2"/>
    <ellipse cx="48" cy="54" rx="28" ry="3" fill="#d6eef8"/>
  </svg>

  <div class="rule" style="left:590px;top:460px;width:402px"></div>

  <div class="receipt"><p>Insert Receipt Here</p></div>
</div>
</body>
</html>
```